Direct to Consumer extended service contract business with a new disruptive business model needs a

We need a customized wordpress design for a company called 'Tall Harbor Assurance'.
We provide an innovative and unique service contract protection program direct to consumers. This program provides monthly coverage for all electronics purchased in the last 4 years and all electronics the consumer purchases in the future for a low monthly fee. The overall design should communicate a sense of legitimacy, ethics, and superior customer service and support (in an industry that has a huge PR issue to overcome).
Electronics is the first product group, other product groups with different price points to launch in the future..

Target Market(s)

All purchasers of electronic goods...all demographics

Industry/Entity Type

Electronics

Font styles to use
Sans Serif

Requirements
Must have
• Customer Testimonials
Industry News
Customer ratings
Blog posts
Call to action messaging
Like the functional elements and design of bramblequill.example (need to be better)
Nice to have
• Like to see video testimonials
Social network "whats trending related to electronics or service contract industry"
Easy way to register products for warranty

```html
<!DOCTYPE html>
<html lang="en">
<head>
<meta charset="utf-8">
<title>Tall Harbor Assurance</title>
<link rel="stylesheet" href="https://fonts.googleapis.com/css2?family=Open+Sans:ital,wght@0,400;0,600;0,700;1,400&family=Oswald:wght@500&family=Raleway:wght@500;600&family=Ubuntu:wght@500;700&display=swap">
<style>
:root{
  --orange:#f47c14;
  --orange-dark:#e2650a;
  --blue:#1a8fe0;
  --blue-bright:#1e9bf0;
  --ink:#2b2b2b;
  --text:#555;
  --muted:#888;
  --rule:#d6d6d6;
  --page:#f1f1f1;
  --band:#e9e9e9;
  --nav:#2f2f2f;
}
*{box-sizing:border-box;margin:0;padding:0}
html,body{width:746px;height:1200px;overflow:hidden}
body{position:relative;background:var(--page);font-family:"Open Sans",sans-serif;color:var(--text)}
.abs{position:absolute}
.topline{left:0;top:0;width:746px;height:3px;background:var(--blue)}
.header{left:0;top:3px;width:746px;height:92px;background:#fff}
.brand{left:72px;top:14px;color:var(--orange);font-family:"Ubuntu",sans-serif;font-weight:700;font-size:21px;line-height:22px}
.brand-mark{display:inline-block;width:12px;height:12px;background:var(--orange);border-radius:50%;margin-right:6px;vertical-align:1px}
.social-top{left:556px;top:16px;display:flex;gap:6px}
.dot{width:24px;height:24px;border-radius:50%;border:2px solid var(--orange)}
.dot.solid{background:#2d5c9e;border-color:#2d5c9e}
.phone{left:558px;top:48px;font-family:"Ubuntu",sans-serif;font-weight:700;font-size:16px;color:var(--ink);display:flex;align-items:center;gap:5px}
.nav{left:74px;top:80px;width:598px;height:34px;background:var(--nav);border-radius:3px;display:flex;font-size:9.5px;font-weight:700;color:#fff;padding:2px}
.nav span{display:flex;align-items:center;padding:0 9.5px;border-right:1px solid #444}
.nav .on{background:var(--orange);border-radius:2px}
.nav .auth{margin-left:auto;background:var(--blue-bright);border:none;padding:0 12px;gap:18px;font-size:10px;border-radius:2px}
.subnav{left:84px;top:124px;display:flex;font-family:"Raleway",sans-serif;font-size:11px;font-weight:500;color:var(--ink)}
.subnav span{padding:0 9px;height:24px;display:flex;align-items:center;gap:4px;border-right:1px solid #bbb}
.subnav span:last-child{border:none}
.subnav .hot{color:var(--orange)}
.hero{left:74px;top:148px;width:414px;height:212px;background:linear-gradient(120deg,#e8e8e8,#cfd3d6 60%,#bfc4c8);box-shadow:0 8px 8px -6px rgba(0,0,0,.35)}
.hero-shot{left:270px;top:30px;width:140px;height:150px;background:linear-gradient(160deg,#8fb5cc,#4a6f8a 55%,#9aa0a4);border-radius:6px}
.hero h1{position:absolute;left:18px;top:32px;font-family:"Ubuntu",sans-serif;font-weight:700;font-size:26px;color:var(--ink)}
.hero h2{position:absolute;left:18px;top:70px;font-family:"Ubuntu",sans-serif;font-weight:700;font-size:23px;color:var(--blue);line-height:29px}
.hero h2 small{display:block;font-size:18.5px}
.quote{left:488px;top:134px;width:185px;height:239px;background:#fff;border:3px solid var(--orange)}
.quote-head{height:40px;background:linear-gradient(#f99a3f,var(--orange-dark));color:#6a2c00;font-family:"Oswald",sans-serif;font-size:15px;padding:8px 9px}
.field{position:absolute;left:15px;width:155px;height:22px;border:1px solid #cfcfcf;font-size:7.5px;font-style:italic;color:#999;padding:5px 7px}
.field .caret{position:absolute;right:0;top:0;width:22px;height:20px;background:#d4d4d4}
.field .caret:after{content:"";position:absolute;left:7px;top:8px;border:4px solid transparent;border-top-color:#fff}
.quote-btn{position:absolute;left:33px;top:209px;width:108px;height:31px;background:var(--blue-bright);color:#fff;font-family:"Oswald",sans-serif;font-size:16px;text-align:center;line-height:31px}
.sec-title{font-family:"Raleway",sans-serif;font-weight:500;font-size:14.5px;color:var(--blue);text-transform:uppercase}
.rule{height:1px;background:var(--rule)}
.rule:before{content:"";display:block;width:60px;height:3px;background:var(--orange);margin-top:-1px}
.rating{width:140px}
.stars{display:flex;gap:4px}
.card-title{color:var(--blue);font-weight:600;font-size:11.5px;margin-top:5px}
.small{font-size:7.6px;line-height:12px;color:var(--text)}
.more{font-size:7.2px;font-style:italic;color:var(--orange);font-weight:600}
.video{left:73px;top:566px;width:227px;height:126px;background:linear-gradient(135deg,#3b3b3b,#6d6f72 50%,#2e2e2e)}
.play{position:absolute;width:42px;height:28px;background:#d8161c;border-radius:3px}
.play:after{content:"";position:absolute;left:16px;top:8px;border:6px solid transparent;border-left:11px solid #fff;border-right:0}
.about{left:324px;top:564px;width:348px;font-size:7.5px;line-height:14.4px;color:#777}
.feed-head{font-weight:600;font-size:9.5px;color:#666;line-height:10px;text-transform:uppercase;display:flex;gap:6px}
.feed-icon{width:16px;height:18px;background:#3b6fb5;border-radius:2px}
.blog-img{width:79px;height:62px;background:linear-gradient(150deg,#9bb4c8,#c9a98c 55%,#6c7f8f)}
.blog-title{color:var(--blue);font-size:9.5px;font-weight:600}
.date{font-size:9px;font-style:italic;color:#555;display:flex;align-items:center;gap:5px}
.fb{left:280px;top:750px;width:186px;height:157px;background:#fff;border:1px solid #3b6fb5}
.tw{left:487px;top:750px;width:187px;height:156px;background:#fff;border:1px solid #d0d0d0}
.avatar{position:absolute;width:30px;height:30px;background:linear-gradient(160deg,#b89a84,#6f6a70)}
.name{position:absolute;width:30px;text-align:center;font-size:5.5px;color:#777}
.band{left:0;top:934px;width:746px;height:208px;background:var(--band)}
.news{width:132px}
.news-img{height:67px;background:linear-gradient(150deg,#8fa7bd,#c8c2b8 55%,#5d6b78);position:relative}
.news-title{font-size:9.5px;color:#444;margin-top:13px}
.news-date{font-size:8.5px;font-weight:700;color:var(--orange);margin-top:6px}
.footer{left:0;top:1142px;width:746px;height:58px;background:var(--blue-bright);border-top:4px solid #2a2d33}
.flinks{position:absolute;left:73px;top:14px;font-size:7.5px;color:#fff;display:flex}
.flinks span{padding:0 6px;border-right:1px solid rgba(255,255,255,.6);line-height:8px}
.flinks span:first-child{padding-left:0}
.flinks span:last-child{border:none}
.copy{position:absolute;left:73px;top:32px;font-size:7.5px;color:#dbeeff}
.fsocial{position:absolute;left:560px;top:16px;display:flex;gap:6px}
.fsocial i{width:22px;height:22px;border:2px solid #fff;border-radius:50%}
</style>
</head>
<body>
<svg width="0" height="0" style="position:absolute">
  <symbol id="star" viewBox="0 0 20 20"><path d="M10 1l2.6 6 6.4.5-4.9 4.2 1.5 6.3L10 14.6 4.4 18l1.5-6.3L1 7.5 7.4 7z" fill="#f47c14"/></symbol>
  <symbol id="cal" viewBox="0 0 12 12"><rect x="1" y="2" width="10" height="9" fill="none" stroke="#888"/><path d="M1 5h10M4 1v2M8 1v2" stroke="#888"/></symbol>
</svg>

<div class="abs topline"></div>
<header class="abs header"></header>
<div class="abs brand"><span class="brand-mark"></span>Tall Harbor<br>Assurance</div>
<div class="abs social-top"><i class="dot solid"></i><i class="dot"></i><i class="dot"></i><i class="dot"></i></div>
<div class="abs phone">
  <svg width="14" height="14" viewBox="0 0 14 14"><path d="M3 1l2.5 3-1.5 1.5c.8 1.8 2.1 3.1 3.9 3.9L9.5 8l3 2.5-1.5 2.5C6 13 1 8 1 3z" fill="var(--blue)"/></svg>
  555.010.4820
</div>

<nav class="abs nav">
  <span class="on">MOBILES</span><span>SLATES</span><span>LAPTOPS</span><span>TABLETS</span><span>SMARTPHONES</span><span>CAMERAS</span><span style="border:none">TELEVISIONS</span>
  <span class="auth"><b>LOGIN</b><b>REGISTER</b></span>
</nav>

<div class="abs subnav">
  <span class="hot"><svg width="9" height="11" viewBox="0 0 9 11"><rect x="1" y="5" width="7" height="5" fill="none" stroke="#f47c14" stroke-width="1.4"/><path d="M2.5 5V3a2 2 0 014 0v2" fill="none" stroke="#f47c14" stroke-width="1.4"/></svg>REGISTER A PLAN</span>
  <span><svg width="11" height="11" viewBox="0 0 11 11"><circle cx="5.5" cy="5.5" r="4.3" fill="none" stroke="#333" stroke-width="1.5"/><circle cx="5.5" cy="5.5" r="1.6" fill="#333"/></svg>MY PLANS</span>
  <span><svg width="12" height="11" viewBox="0 0 12 11"><rect x="1" y="2" width="8" height="8" fill="none" stroke="#333" stroke-width="1.3"/><path d="M5 7l6-6" stroke="#333" stroke-width="1.5"/></svg>FILE A CLAIM</span>
</div>

<section class="abs hero">
  <div class="abs hero-shot" role="img" aria-label="Open laptop with a colourful screen"></div>
  <h1>PROTECT LAPTOP</h1>
  <h2>SAVE UP TO 60% VS.<small>YOUR CURRENT&nbsp; LAPTOP</small></h2>
</section>

<form class="abs quote">
  <div class="quote-head">GET A QUOTE TODAY</div>
  <div class="field" style="top:55px">What phone do you have?<span class="caret"></span></div>
  <div class="field" style="top:93px">Where did you buy it?<span class="caret"></span></div>
  <div class="field" style="top:132px">Email me this quote( Optional )</div>
  <div class="field" style="top:170px">Email me this quote( Optional )</div>
  <div class="quote-btn">GET A QUOTE</div>
</form>

<h3 class="abs sec-title" style="left:73px;top:400px">Our Customer Ratings</h3>
<div class="abs rule" style="left:73px;top:424px;width:599px"></div>

<div class="abs rating" style="left:73px;top:437px">
  <div class="stars"><svg width="17" height="17"><use href="#star"/></svg><svg width="17" height="17"><use href="#star"/></svg><svg width="17" height="17"><use href="#star"/></svg><svg width="17" height="17"><use href="#star"/></svg><svg width="17" height="17"><use href="#star"/></svg></div>
  <div class="card-title">Orchard App Market</div><div class="small" style="margin-top:4px">Lorem ipsum dolor sit amet</div><div class="more" style="margin-top:4px">Read more ›</div>
</div>
<div class="abs rating" style="left:240px;top:437px">
  <div class="stars"><svg width="17" height="17"><use href="#star"/></svg><svg width="17" height="17"><use href="#star"/></svg><svg width="17" height="17"><use href="#star"/></svg><svg width="17" height="17"><use href="#star"/></svg><svg width="17" height="17"><use href="#star"/></svg></div>
  <div class="card-title">Orchard App Market</div><div class="small" style="margin-top:4px">Lorem ipsum dolor sit amet</div><div class="more" style="margin-top:4px">Read more ›</div>
</div>
<div class="abs rating" style="left:406px;top:437px">
  <div class="stars"><svg width="17" height="17"><use href="#star"/></svg><svg width="17" height="17"><use href="#star"/></svg><svg width="17" height="17"><use href="#star"/></svg><svg width="17" height="17"><use href="#star"/></svg><svg width="17" height="17"><use href="#star"/></svg></div>
  <div class="card-title">Orchard App Market</div><div class="small" style="margin-top:4px">Lorem ipsum dolor sit amet</div><div class="more" style="margin-top:4px">Read more ›</div>
</div>
<div class="abs rating" style="left:573px;top:437px">
  <div class="stars"><svg width="17" height="17"><use href="#star"/></svg><svg width="17" height="17"><use href="#star"/></svg><svg width="17" height="17"><use href="#star"/></svg><svg width="17" height="17"><use href="#star"/></svg><svg width="17" height="17"><use href="#star"/></svg></div>
  <div class="card-title">Orchard App Market</div><div class="small" style="margin-top:4px">Lorem ipsum dolor sit amet</div><div class="more" style="margin-top:4px">Read more ›</div>
</div>

<h3 class="abs sec-title" style="left:73px;top:529px">Our Customers Stories</h3>
<div class="abs rule" style="left:73px;top:552px;width:227px"></div>
<div class="abs video" role="img" aria-label="Video testimonial grid of customer photos"><span class="play" style="left:93px;top:49px"></span></div>

<h3 class="abs sec-title" style="left:324px;top:529px">About Tall Harbor Assurance</h3>
<div class="abs rule" style="left:324px;top:552px;width:348px"></div>
<p class="abs about">Lorem ipsum dolor sit amet, consectetur adipiscing elit. Fusce ornare congue velit vitae aliquet. Nam ipsum lectus, interdum id ipsum eu, imperdiet dictum odio. Interdum et malesuada fames ac ante ipsum primis in faucibus. Aliquam in ex urna. Sed est massa, dignissim non dignissim viverra, cursus id ligula. Nullam non ex sit amet arcu vulputate placerat. Vestibulum porttitor, odio ac dignissim consectetur, mi odio condimentum ipsum, non consequat ex dui nec leo. Vestibulum a ipsum vel ex pellentesque tincidunt. Curabitur eget feugiat dolor. Vivamus mauris felis, vestibulum non suscipit quis, egestas et est. Aliquam quis sollicitudin tellus. Integer facilisis finibus lectus, consequat lobortis nulla rutrum e sed at diam. Donec id risus odio.<br><span class="more" style="display:inline-block;margin-top:4px">Read more</span></p>

<h3 class="abs sec-title" style="left:73px;top:713px">Blog Posts</h3>
<div class="abs rule" style="left:73px;top:736px;width:187px"></div>

<div class="abs blog-img" style="left:73px;top:750px" role="img" aria-label="Portrait of a smiling woman"></div>
<div class="abs" style="left:159px;top:749px;width:105px">
  <div class="blog-title">Lorem ipsum dolor sit</div>
  <div class="date" style="margin-top:6px"><svg width="12" height="12"><use href="#cal"/></svg>28 / Aug / 2014</div>
  <div class="small" style="margin-top:7px">consectetur adipiscing elit. Donec dignissim diavel</div>
</div>
<div class="abs blog-img" style="left:73px;top:826px" role="img" aria-label="Portrait of a smiling man"></div>
<div class="abs" style="left:159px;top:825px;width:105px">
  <div class="blog-title">Lorem ipsum dolor sit</div>
  <div class="date" style="margin-top:6px"><svg width="12" height="12"><use href="#cal"/></svg>28 / Aug / 2014</div>
  <div class="small" style="margin-top:7px">consectetur adipiscing elit. Donec dignissim diavel</div>
</div>
<div class="abs more" style="left:199px;top:899px">Read more blog</div>

<div class="abs feed-head" style="left:282px;top:717px"><i class="feed-icon"></i><span>Be the first to know it<br>all on our page</span></div>
<div class="abs feed-head" style="left:487px;top:717px"><i class="feed-icon" style="background:#2ea5e8"></i><span>See what we've been up<br>to on our feed</span></div>

<div class="abs fb">
  <div style="position:absolute;left:11px;top:8px;font-size:8px;font-weight:700;color:#3b5a8c">Tall Harbor Assurance</div>
  <div style="position:absolute;left:11px;top:22px;font-size:6px;color:#444;display:flex;gap:5px;align-items:center"><span style="border:1px solid #ccc;padding:1px 4px;color:#999">✓ Like</span>You like this.</div>
  <div style="position:absolute;left:11px;top:38px;width:162px;height:1px;background:#ddd"></div>
  <div style="position:absolute;left:11px;top:44px;font-size:6px;color:#333">1,360 people like <b>Tall Harbor Assurance</b></div>
  <div class="avatar" style="left:11px;top:56px" role="img" aria-label="Follower photo"></div><div class="name" style="left:11px;top:88px">Ines</div>
  <div class="avatar" style="left:44px;top:56px" role="img" aria-label="Follower photo"></div><div class="name" style="left:44px;top:88px">Theo</div>
  <div class="avatar" style="left:77px;top:56px" role="img" aria-label="Follower photo"></div><div class="name" style="left:77px;top:88px">Mara</div>
  <div class="avatar" style="left:110px;top:56px" role="img" aria-label="Follower photo"></div><div class="name" style="left:110px;top:88px">Lena</div>
  <div class="avatar" style="left:143px;top:56px" role="img" aria-label="Follower photo"></div><div class="name" style="left:143px;top:88px">Pia</div>
  <div class="avatar" style="left:11px;top:100px" role="img" aria-label="Follower photo"></div><div class="name" style="left:11px;top:132px">Ole</div>
  <div class="avatar" style="left:44px;top:100px" role="img" aria-label="Follower photo"></div><div class="name" style="left:44px;top:132px">Lena</div>
  <div class="avatar" style="left:77px;top:100px" role="img" aria-label="Follower photo"></div><div class="name" style="left:77px;top:132px">Ada</div>
  <div class="avatar" style="left:110px;top:100px" role="img" aria-label="Follower photo"></div><div class="name" style="left:110px;top:132px">Kenji</div>
  <div class="avatar" style="left:143px;top:100px" role="img" aria-label="Follower photo"></div><div class="name" style="left:143px;top:132px">Hugo</div>
  <div style="position:absolute;left:11px;top:144px;font-size:5.5px;color:#666;display:flex;gap:3px;align-items:center"><i style="width:7px;height:7px;background:#3b6fb5"></i>Social plugin</div>
</div>

<div class="abs tw">
  <div style="position:absolute;left:10px;top:8px;font-size:8px;font-weight:700;color:#333">Posts</div>
  <div style="position:absolute;right:10px;top:6px;font-size:6.5px;font-weight:600;color:#2a5f8f;border:1px solid #ccc;border-radius:2px;padding:1px 4px;background:#eef4fa">Follow</div>
  <div style="position:absolute;left:0;top:24px;width:185px;height:1px;background:#ddd"></div>
  <div class="avatar" style="left:7px;top:28px;width:27px;height:27px" role="img" aria-label="Account photo"></div>
  <div style="position:absolute;left:39px;top:29px;width:130px;font-size:7.5px;color:#333;font-weight:600">Wren Castell<span style="float:right;font-weight:400;color:#888">10h</span></div>
  <div style="position:absolute;left:39px;top:42px;font-size:6.5px;color:#777">@loremispumdolor</div>
  <div style="position:absolute;left:7px;top:56px;font-size:6.5px;color:#555">Lorem ipsum dolor sit amet, consectetur</div>
  <div style="position:absolute;left:7px;top:68px;font-size:6px;color:#888">▣ Show Photo</div>
  <div style="position:absolute;left:0;top:81px;width:178px;height:1px;background:#ddd"></div>
  <div class="avatar" style="left:7px;top:84px;width:27px;height:27px" role="img" aria-label="Account photo"></div>
  <div style="position:absolute;left:39px;top:85px;width:130px;font-size:7.5px;color:#333;font-weight:600">Wren Castell<span style="float:right;font-weight:400;color:#888">10h</span></div>
  <div style="position:absolute;left:39px;top:98px;font-size:6.5px;color:#777">@loremispumdolor</div>
  <div style="position:absolute;left:7px;top:112px;font-size:6.5px;color:#555">Lorem ipsum dolor sit amet, consectetur</div>
  <div style="position:absolute;left:7px;top:124px;font-size:6px;color:#888">▣ Show Photo</div>
  <div style="position:absolute;left:177px;top:26px;width:7px;height:110px;border-left:1px solid #ddd"></div>
  <div style="position:absolute;left:3px;top:138px;width:179px;height:15px;border:1px solid #ccc;font-size:6.5px;color:#666;padding:2px 6px">Message @loremispumdolor</div>
</div>

<section class="abs band"></section>
<h3 class="abs sec-title" style="left:73px;top:955px">Industry Breaking News</h3>
<div class="abs rule" style="left:73px;top:978px;width:185px"></div>

<article class="abs news" style="left:73px;top:992px">
  <div class="news-img" role="img" aria-label="Businesswoman smiling in an office"></div>
  <div class="news-title" style="color:var(--blue)">Lorem ipsum dolor site amet</div>
  <div class="news-date">20. 07. 2014</div>
  <div class="small" style="margin-top:6px">lorem ispum consecter adipiscing elit. Donec dignissim diavel</div>
</article>
<article class="abs news" style="left:229px;top:992px">
  <div class="news-img" role="img" aria-label="Business team standing by a glass wall"></div>
  <div class="news-title">Lorem ipsum dolor site amet</div>
  <div class="news-date">20. 07. 2014</div>
  <div class="small" style="margin-top:6px">lorem ispum consecter adipiscing elit. Donec dignissim diavel</div>
</article>
<article class="abs news" style="left:385px;top:992px">
  <div class="news-img" role="img" aria-label="Support agent wearing a headset"><span class="play" style="left:52px;top:25px;width:28px;height:18px"></span></div>
  <div class="news-title">Lorem ipsum dolor site amet</div>
  <div class="news-date">20. 07. 2014</div>
  <div class="small" style="margin-top:6px">lorem ispum consecter adipiscing elit. Donec dignissim diavel</div>
</article>
<article class="abs news" style="left:541px;top:992px">
  <div class="news-img" role="img" aria-label="Colleagues working on a laptop outdoors"><span class="play" style="left:52px;top:25px;width:28px;height:18px"></span></div>
  <div class="news-title">Lorem ipsum dolor site amet</div>
  <div class="news-date">20. 07. 2014</div>
  <div class="small" style="margin-top:6px">lorem ispum consecter adipiscing elit. Donec dignissim diavel</div>
</article>

<footer class="abs footer">
  <div class="flinks"><span>HOME</span><span>ABOUT US</span><span>BLOG</span><span>CONTACT US</span><span>LOGIN</span><span>SIGN UP</span></div>
  <div class="copy">Copyright © 2014 <b style="color:#fff;font-weight:600">Tall Harbor Assurance.</b> &nbsp;&nbsp;<span style="color:#fff">Terms</span> &nbsp;|&nbsp; Privacy</div>
  <div class="fsocial"><i></i><i></i><i></i><i></i></div>
</footer>
</body>
</html>
```